Water Filter Company Needs Bizz Cards!!

Need business cards for my company. We sell whole home water filters and salt free water softeners. No more buying bottled water. Our filtering units filter out all heavy metals, chlorine, and VOC's, last 15 years, and are maintenance free and supply your whole home with spring quality alkaline water. Our Salt free water conditioners, eliminate hard water and scale, without lowering the ph, or TDS's (total Dissolved solids)

I think this is the color code we are using on my site. My logo looks good behind it. #192841

Website will be www.Brovexa.com

Industry/Entity Type

Water Purification

Contact Information for Business Card

For now, just insert standard Dummy text. I need these text lines for the info to be editable so i can make them for multiple employees. I do have Photoshop and illustrator, unless there is a simpler program i can use solely for biz cards

Font styles to use
Sans Serif

Requirements
Must have
• Use my preexisting logo.

www.BroVexa.com

Spring Quality Alkaline Water at every tap.

List out services. Whole Home Water Filters, Salt Free Water Softeners, Clarimont KT7, UV Sterilizers
Nice to have
• I think this is the color code we are using on my site. My logo looks good behind it. #192841 or black. Please no white or light blue backgrounds.

Maybe a picture of my tank.

Slogan like Spring Quality Alkaline Water at every tap.
And just list the services Whole Home Water Filters, Salt Free Water Softeners, Clarimont KT7, UV Sterilizers

I think I would like to not have a contrasting textured logo like I see on some of them. I may use it for my personal cards, but new employees may not want the extra expense.
Should not have
• A different logo than the one provided.

White or baby blue backgrounds. Use the color code, or blacks.

```html
<!DOCTYPE html>
<html lang="en">
<head>
<meta charset="utf-8">
<title>Brovexa Business Card</title>
<link href="https://fonts.googleapis.com/css2?family=Poppins:wght@400;500;600;700&family=Great+Vibes&display=swap" rel="stylesheet">
<style>
  :root {
    --page-bg: #e8e5e0;
    --card-bg: #192841;
    --brand-blue: #34aee8;
    --deep-blue: #1b8fd6;
    --sky-blue: #4fc0ef;
    --wave-gray: #8e96a3;
    --text-light: #d3d7dd;
    --name-light: #c9ced6;
    --rule-line: #4a5a75;
    --photo-light: #2a3c5c;
    --photo-mid: #3a4f74;
    --white: #ffffff;
  }
  * { box-sizing: border-box; margin: 0; padding: 0; }
  html, body { width: 900px; height: 1200px; overflow: hidden; }
  body { background: var(--page-bg); font-family: "Poppins", sans-serif; position: relative; }

  .card {
    position: absolute; left: 80px; width: 733px; height: 428px;
    background: var(--card-bg); border-radius: 22px; overflow: hidden;
    box-shadow: 0 6px 18px rgba(0,0,0,0.25);
  }
  .card--front { top: 128px; }
  .card--back { top: 646px; }

  .waves { position: absolute; inset: 0; width: 100%; height: 100%; }

  .brand { position: absolute; display: flex; align-items: center; gap: 12px; }
  .brand__dot { width: 30px; height: 30px; border-radius: 50%; background: var(--brand-blue); }
  .brand__name { font-weight: 600; font-size: 50px; color: var(--brand-blue); letter-spacing: -1px; line-height: 1; }
  .card--front .brand { left: 40px; top: 36px; }
  .card--back .brand { left: 40px; top: 62px; }

  .services { position: absolute; left: 40px; top: 204px; list-style: none; }
  .services li {
    display: flex; align-items: center; gap: 8px;
    font-weight: 500; font-size: 16.5px; color: var(--sky-blue); height: 28.5px;
  }
  .services li::before {
    content: ""; width: 9px; height: 9px; border-radius: 50%; background: var(--brand-blue);
  }

  .product-photo {
    position: absolute; left: 425px; top: 20px; width: 285px; height: 315px;
    background: radial-gradient(ellipse at 50% 60%, var(--photo-mid), rgba(42,60,92,0) 72%);
    border-radius: 10px;
  }

  .slogan {
    position: absolute; left: 0; right: 0; bottom: 8px; text-align: center;
    font-family: "Great Vibes", cursive; font-size: 22px; color: var(--white);
  }

  .person { position: absolute; right: 44px; top: 66px; text-align: right; }
  .person__name { font-weight: 700; font-size: 27px; color: var(--name-light); line-height: 1.1; }
  .person__name span { color: var(--brand-blue); }
  .person__role { font-weight: 500; font-size: 16px; color: var(--brand-blue); }

  .rule { position: absolute; left: 42px; right: 44px; top: 285px; height: 2px; background: var(--rule-line); }

  .contacts { position: absolute; left: 42px; top: 296px; list-style: none; }
  .contacts li {
    display: flex; align-items: center; gap: 9px;
    font-size: 16px; color: var(--text-light); height: 25px;
  }
  .contacts svg { width: 14px; height: 14px; flex: none; }

  .address {
    position: absolute; right: 44px; top: 296px; text-align: right;
    font-size: 16px; color: var(--text-light); line-height: 25px;
  }
</style>
</head>
<body>

<section class="card card--front">
  <svg class="waves" viewBox="0 0 733 428" preserveAspectRatio="none" aria-hidden="true">
    <path d="M0,112 C120,160 280,175 420,120 S640,40 733,92 L733,112 C640,62 500,120 420,142 S130,190 0,142 Z" fill="var(--wave-gray)"/>
    <path d="M0,98 C120,145 280,160 420,104 S640,28 733,76 L733,94 C640,46 500,102 420,124 S120,170 0,116 Z" fill="var(--deep-blue)"/>
    <path d="M0,356 C200,330 450,325 733,352 L733,428 L0,428 Z" fill="var(--wave-gray)"/>
    <path d="M0,388 C220,352 480,345 733,370 L733,428 L0,428 Z" fill="var(--sky-blue)"/>
    <path d="M0,405 C240,375 500,372 733,392 L733,428 L0,428 Z" fill="var(--deep-blue)"/>
  </svg>

  <div class="brand">
    <span class="brand__dot"></span>
    <span class="brand__name">Brovexa</span>
  </div>

  <ul class="services">
    <li>Whole home water filters</li>
    <li>Salt free water softeners</li>
    <li>Clarimont KT7</li>
    <li>UV Sterilizers</li>
  </ul>

  <div class="product-photo" role="img" aria-label="Product photo of three water treatment units: a black filter tank, a beige softener tank and a UV sterilizer"></div>

  <p class="slogan">Spring Quality Alkaline Water at every tap</p>
</section>

<section class="card card--back">
  <div class="brand">
    <span class="brand__dot"></span>
    <span class="brand__name">Brovexa</span>
  </div>

  <div class="person">
    <p class="person__name">Daniel <span>Reyes</span></p>
    <p class="person__role">Director</p>
  </div>

  <div class="rule"></div>

  <ul class="contacts">
    <li>
      <svg viewBox="0 0 24 24" aria-hidden="true"><path fill="var(--brand-blue)" d="M6.6 10.8a15.1 15.1 0 0 0 6.6 6.6l2.2-2.2a1 1 0 0 1 1-.25 11.4 11.4 0 0 0 3.6.57 1 1 0 0 1 1 1V20a1 1 0 0 1-1 1A17 17 0 0 1 3 4a1 1 0 0 1 1-1h3.5a1 1 0 0 1 1 1c0 1.25.2 2.45.57 3.57a1 1 0 0 1-.25 1z"/></svg>
      0987 654 321
    </li>
    <li>
      <svg viewBox="0 0 24 24" aria-hidden="true"><rect x="2" y="5" width="20" height="14" fill="var(--brand-blue)"/><path d="M3 6l9 7 9-7" fill="none" stroke="var(--card-bg)" stroke-width="1.6"/></svg>
      hello@brovexa.com
    </li>
    <li>
      <svg viewBox="0 0 24 24" aria-hidden="true"><circle cx="12" cy="12" r="9" fill="none" stroke="var(--brand-blue)" stroke-width="2"/><ellipse cx="12" cy="12" rx="4" ry="9" fill="none" stroke="var(--brand-blue)" stroke-width="1.6"/><path d="M3 12h18M5 7.5h14M5 16.5h14" stroke="var(--brand-blue)" stroke-width="1.4"/></svg>
      www.Brovexa.com
    </li>
  </ul>

  <p class="address">4820 Harbor Lane<br>Portland OR, USA</p>
</section>

</body>
</html>
```